Business Card Design For A Renovation Contractor Company

We need a business card for a new company based in Singapore, our company name is "KT Planora". We are a renovation contractor that builds designs into reality. We build more of F&B restaurants, retail stores and commercial offices. We work very closely with designers. The final design should communicate to our client that we are a company that you can trust, that will plan and complete your project without giving you a headache. I like my client to remember my company as "KT". The beauty of SIMPLE is important.

Industry/Entity Type

Contractor

Requirements
Nice to have
• Black or Red base

```html
<!DOCTYPE html>
<html lang="en">
<head>
<meta charset="utf-8">
<title>KT Planora — Business Card</title>
<link rel="stylesheet" href="https://fonts.googleapis.com/css2?family=Questrial&family=Open+Sans:wght@400;600&display=swap">
<style>
  :root {
    --backdrop: #2b2b2d;
    --red: #e81e25;
    --black: #0f0f10;
    --card-light: #e9e9ea;
    --ink: #1b1b1b;
    --white: #f4f4f4;
    --rule-grey: #8a8a8a;
  }
  * { box-sizing: border-box; margin: 0; padding: 0; }
  html, body { width: 1200px; height: 900px; overflow: hidden; }
  body {
    background: var(--backdrop);
    font-family: "Open Sans", Arial, sans-serif;
    position: relative;
  }
  .card {
    position: absolute;
    top: 300px;
    width: 500px;
    height: 300px;
    border-radius: 26px;
    overflow: hidden;
    box-shadow: 0 14px 30px rgba(0,0,0,.45);
  }
  /* front */
  .card-front { left: 70px; background: var(--black); }
  .card-front .band { position: absolute; left: 0; right: 0; height: 48px; background: var(--red); }
  .card-front .band-top { top: 0; }
  .card-front .band-bottom { bottom: 0; }
  .card-front .rule { position: absolute; left: 0; right: 0; height: 1px; background: var(--rule-grey); }
  .card-front .rule-top { top: 58px; }
  .card-front .rule-bottom { bottom: 58px; }

  .brand {
    position: absolute;
    left: 0; right: 0;
    display: flex; flex-direction: column; align-items: center;
    font-family: "Questrial", "Century Gothic", sans-serif;
  }
  .brand-mark {
    width: 56px; height: 56px; border-radius: 50%;
    border: 5px solid var(--red);
    margin-bottom: 8px;
  }
  .brand-name {
    font-size: 48px; line-height: 1; letter-spacing: -0.5px;
    padding: 0 6px 3px;
    border-bottom: 1.5px solid currentColor;
  }
  .brand-tagline { font-size: 17px; margin-top: 2px; }

  .card-front .brand { top: 78px; color: var(--white); }

  /* back */
  .card-back { left: 630px; background: var(--card-light); }
  .card-back .brand { top: 36px; color: var(--ink); }
  .card-back .brand-mark { width: 46px; height: 46px; border-width: 4px; margin-bottom: 6px; }
  .card-back .brand-name { font-size: 38px; }
  .card-back .brand-tagline { font-size: 14px; }

  .contact {
    position: absolute; left: 0; right: 0; top: 168px;
    text-align: center; color: var(--ink);
  }
  .contact-name { color: var(--red); font-size: 15px; letter-spacing: .5px; }
  .contact-role { font-size: 11px; margin-bottom: 6px; }
  .contact-address { font-size: 10.5px; margin-bottom: 6px; }
  .contact-lines { font-size: 11px; line-height: 1.35; }
  .contact-lines .label { color: var(--red); }
  .contact-lines .gap { display: inline-block; width: 14px; }

  .strip {
    position: absolute; left: 0; right: 0; bottom: 0; height: 22px;
    background: var(--black);
  }
  .strip .seg { position: absolute; top: 0; bottom: 0; background: var(--red); }
  .strip .seg-a { left: 22%; width: 28%; }
  .strip .seg-b { right: 0; width: 22%; }
</style>
</head>
<body>
  <section class="card card-front" aria-label="Business card front">
    <div class="band band-top"></div>
    <div class="rule rule-top"></div>
    <div class="brand">
      <div class="brand-mark"></div>
      <div class="brand-name">KT Planora</div>
      <div class="brand-tagline">planned well, built with care</div>
    </div>
    <div class="rule rule-bottom"></div>
    <div class="band band-bottom"></div>
  </section>

  <section class="card card-back" aria-label="Business card back">
    <div class="brand">
      <div class="brand-mark"></div>
      <div class="brand-name">KT Planora</div>
      <div class="brand-tagline">planned well, built with care</div>
    </div>
    <div class="contact">
      <p class="contact-name">MARA LINDQVIST</p>
      <p class="contact-role">Manager</p>
      <p class="contact-address">Address 18 Kerrow Lane, 0427 Harlow Quay, Singapore 240118</p>
      <p class="contact-lines"><span class="label">mobile:</span> 6590012478<span class="gap"></span><span class="label">phone:</span> 6590036215</p>
      <p class="contact-lines"><span class="label">email:</span> mara@ktplanora.com<span class="gap"></span><span class="label">web:</span> www.ktplanora.com</p>
    </div>
    <div class="strip"><div class="seg seg-a"></div><div class="seg seg-b"></div></div>
  </section>
</body>
</html>
```